Emergency Medical Training and Events Company Business Needs Business Card Design

We are in need of a business card for our dynamic company expanding its customer base and need to be easily contacted and identified for when we visit with government officials, potential EMS / Fire agencies and county coordinators to arrange for training programs for first responders to better prepare them for critical thinking at critical incidents.

Target Market(s)

EMS/Fire and Event Promoters

Industry/Entity Type

Medical

Contact Information for Business Card

Two cards, comparable designs:

Martin K. Halvey, Principal, m.halvey@rvqtlo.com
Owen Tash, Event and Training Specialist, o.tash@rvqtlo.com

Font styles to use
Other font styles liked:
• Cambria

Colors

Designer to choose colors to be used in the design.

Requirements
Must have
• Company Logo, Spots for Name, Title, Phone Number, Email, Website
• A bullet list stating that we offer, QRB CPR and First Aid Instructors, Hold the Line Instructors, Event EMS, CME's, MCI Training and Planning. We prefer to have a black background for the card but if you can make a blue or white card stand out we would review that as well.
Should not have
• Tacky logos or special sayings ... simple, elegant, professional is the look we seek

```html
<!DOCTYPE html>
<html lang="en">
<head>
<meta charset="utf-8">
<title>RVQ Solutions – Business Card</title>
<link href="https://fonts.googleapis.com/css2?family=Arimo:wght@400;700&display=swap" rel="stylesheet">
<style>
  :root {
    --navy: #1f2a5c;
    --red: #d62027;
    --ink: #3a3f4a;
    --paper: #ffffff;
    --backdrop: #e9e9eb;
  }
  * { box-sizing: border-box; margin: 0; padding: 0; }
  html, body { width: 1200px; height: 800px; overflow: hidden; }
  body {
    background: var(--backdrop);
    font-family: "Arimo", Arial, sans-serif;
    color: var(--ink);
    position: relative;
  }
  .card {
    position: absolute;
    top: 245px;
    width: 540px;
    height: 310px;
    background: var(--paper);
    border-bottom: 4px solid var(--red);
    box-shadow: 0 6px 18px rgba(0,0,0,0.12);
  }
  .card--front { left: 40px; }
  .card--back { left: 620px; }

  .brand { display: flex; align-items: center; gap: 10px; white-space: nowrap; }
  .brand__dot { width: 30px; height: 30px; border-radius: 50%; background: var(--navy); flex: none; }
  .brand__name { font-weight: 700; color: var(--navy); letter-spacing: 0.5px; }

  /* front */
  .card--front .brand { position: absolute; left: 36px; top: 140px; width: 200px; }
  .card--front .brand__dot { width: 28px; height: 28px; }
  .card--front .brand__name { font-size: 18px; letter-spacing: 0.3px; }
  .divider { position: absolute; left: 255px; top: 60px; width: 1px; height: 190px; background: var(--navy); }
  .contact { position: absolute; left: 278px; top: 62px; }
  .contact__name { color: var(--red); font-weight: 700; font-size: 22px; }
  .contact__title { font-size: 15px; margin-top: 4px; }
  .contact__address { font-size: 14px; margin-top: 10px; line-height: 1.35; }
  .contact__list { list-style: none; margin-top: 14px; font-size: 14px; }
  .contact__list li { display: flex; align-items: center; gap: 8px; margin-bottom: 5px; }
  .contact__list svg { width: 13px; height: 13px; flex: none; }
  .accent { color: var(--red); }

  /* back */
  .card--back .brand { position: absolute; left: 0; right: 0; top: 62px; justify-content: center; }
  .card--back .brand__dot { width: 48px; height: 48px; }
  .card--back .brand__name { font-size: 34px; }
  .services { position: absolute; left: 0; right: 0; top: 170px; list-style: none; text-align: center; font-size: 16px; color: var(--navy); line-height: 1.7; }
  .services li::before { content: "•"; color: var(--red); margin-right: 8px; }
</style>
</head>
<body>
  <section class="card card--front">
    <div class="brand">
      <span class="brand__dot"></span>
      <span class="brand__name">RVQ SOLUTIONS</span>
    </div>
    <div class="divider"></div>
    <div class="contact">
      <p class="contact__name">Martin K. Halvey</p>
      <p class="contact__title">Principal</p>
      <p class="contact__address">Your address, city<br>state, ZIP 0000</p>
      <ul class="contact__list">
        <li><svg viewBox="0 0 16 16"><path fill="#d62027" d="M3 1l3 3-1.5 2a9 9 0 0 0 5.5 5.5L12 10l3 3-2 2C7 15 1 9 1 3z"/></svg><span>555.014.2290</span></li>
        <li><svg viewBox="0 0 16 16"><rect x="1" y="3" width="14" height="10" rx="1" fill="none" stroke="#d62027" stroke-width="1.6"/><path d="M1.5 4l6.5 5 6.5-5" fill="none" stroke="#d62027" stroke-width="1.6"/></svg><span>m.halvey@rvqtlo.com</span></li>
        <li><svg viewBox="0 0 16 16"><circle cx="8" cy="8" r="7" fill="#d62027"/><path d="M1 8h14M8 1c3 3 3 11 0 14M8 1c-3 3-3 11 0 14" fill="none" stroke="#fff" stroke-width="1"/></svg><span>www.<span class="accent">rvqtlo</span>.com</span></li>
      </ul>
    </div>
  </section>

  <section class="card card--back">
    <div class="brand">
      <span class="brand__dot"></span>
      <span class="brand__name">RVQ SOLUTIONS</span>
    </div>
    <ul class="services">
      <li>QRB CPR and First Aid Instructors</li>
      <li>Hold the Line Instructors</li>
      <li>we do Event EMS, CME's, MCI Training and Planning</li>
    </ul>
  </section>
</body>
</html>
```